Detox Drink Needs A Label for a drug testing company

About Us
The company name is “Pillwise”, we are a diagnostic test provider specialising in the distribution and manufacturing of drug testing kits. Our end user is both commercial and private clients with over 70% being the later of the two.

About the product
The product I am marketing is a urine detox drink aimed at removing drug metabolites from the urine, there are currently a number of similar products on the market; Veltroprime, Falcor Brisq, Renoquill, none of which are made in Australia.

We are looking to enter this market with an Australia made and owned product that works in much the same way
but is available locally for distribution.

We currently have another product on the market which works in much the same way but to remove drug metabolites from the saliva in order to prevent false positives on a drugntest.

The urine cleanse will work by diuretic action, promoting urination by osmotic release,effectively diluting drug metabolites.

What we are after
What we are after is a label to suit a 500ML bottle that contains various information including company logo, nutritional Information which will need to be editable, size, flavour etc. Product name – Urine Cleanse / Purge – Lite Flavour – Watermelon , Grape

We would like to keep a professional but modern look that makes our product come across as more pharmaceutical rather than the energy drink look that our competitors are running
with.

Industry/Entity Type

Health Product

Colors
33a6d7
f3f1f8
fbf289
33b8a4

Requirements
Must have
• Flavour; Grape, Watermelon, Lemon Line (must be editable text)
• Brand Logo
• Colorful Graphics
• Full wrap around label
• Nutritional Information on the rear with editable text
• Urine Cleanse
• Helps to cleanse the urine of drug metabolites

```html
<!DOCTYPE html>
<html lang="en">
<head>
<meta charset="utf-8">
<title>Pillwise Urine Cleanse – Watermelon Label</title>
<link rel="stylesheet" href="https://fonts.googleapis.com/css2?family=Open+Sans:wght@600;700;800&display=swap">
<style>
  :root {
    --backdrop: #e4e5ea;
    --label-white: #f3f1f8;
    --teal: #2aa898;
    --yellow: #f0dc5a;
    --red: #c51f2d;
    --ink: #141414;
    --white: #ffffff;
  }
  html, body {
    margin: 0;
    padding: 0;
    width: 768px;
    height: 1200px;
    overflow: hidden;
    background: var(--backdrop);
    font-family: "Open Sans", Arial, sans-serif;
  }
  .label {
    position: absolute;
    left: 39px;
    top: 210px;
    width: 690px;
    height: 790px;
    background: var(--label-white);
    box-shadow: 0 2px 10px rgba(0, 0, 0, 0.12);
  }
  .label h1,
  .label p {
    margin: 0;
  }
  .dot-strip {
    position: absolute;
    left: 60px;
    top: 42px;
    width: 560px;
    height: 46px;
    background: linear-gradient(180deg, var(--teal) 0%, rgba(42,168,152,0.7) 100%);
    opacity: 0.85;
    border-radius: 4px;
  }
  .brand {
    position: absolute;
    left: 0;
    right: 0;
    top: 180px;
    height: 90px;
    display: flex;
    align-items: center;
    justify-content: center;
    gap: 16px;
  }
  .brand-mark {
    width: 40px;
    height: 40px;
    border-radius: 50%;
    background: var(--teal);
  }
  .brand-name {
    font-weight: 700;
    font-size: 52px;
    line-height: 1;
    color: var(--ink);
    letter-spacing: 1px;
  }
  .halftone-field {
    position: absolute;
    left: 78px;
    top: 285px;
    width: 532px;
    height: 150px;
    background: linear-gradient(180deg, var(--teal) 0%, rgba(42,168,152,0.45) 60%, rgba(42,168,152,0.08) 100%);
  }
  .product-name {
    position: absolute;
    left: 0;
    right: 0;
    top: 436px;
    text-align: center;
    font-weight: 800;
    font-size: 70px;
    line-height: 84px;
    color: var(--ink);
    text-shadow: 5px -5px 0 var(--yellow);
    letter-spacing: -1px;
  }
  .claim-band {
    position: absolute;
    left: 88px;
    top: 526px;
    width: 514px;
    height: 104px;
    background: var(--teal);
    color: var(--white);
    display: flex;
    align-items: center;
    justify-content: center;
    text-align: center;
    font-weight: 700;
    font-size: 26px;
    line-height: 1.25;
  }
  .flavour-band {
    position: absolute;
    left: 88px;
    top: 646px;
    width: 514px;
    height: 80px;
    background: var(--red);
    color: var(--white);
    display: flex;
    align-items: center;
    justify-content: center;
    font-weight: 600;
    font-size: 40px;
    line-height: 1;
  }
  .base-stripe {
    position: absolute;
    left: 88px;
    top: 740px;
    width: 514px;
    height: 24px;
    background: var(--teal);
  }
</style>
</head>
<body>
  <main class="label">
    <div class="dot-strip" role="img" aria-label="Row of teal dots along the top of the label"></div>
    <div class="brand">
      <span class="brand-mark"></span>
      <span class="brand-name">Pillwise</span>
    </div>
    <div class="halftone-field" role="img" aria-label="Teal halftone dot pattern fading downward"></div>
    <h1 class="product-name">URINE CLEANSE</h1>
    <p class="claim-band">HELPS TO CLEANSE THE URINE<br>OF DRUG METABOLITES</p>
    <p class="flavour-band">Watermelon</p>
    <div class="base-stripe"></div>
  </main>
</body>
</html>
```